Real Estate Templates in Canva

I need someone to create a robust set of Canva template designs for my real estate company team, to streamline content. I need a catalog for my agents to easily go in and pick from different designs and customize for themselves. The correct candidate can emulate the style found on these sites., and in the attached images. I have also uploaded logos to be used.(https://www.brindlehomegroup.com/) and (https://meetkoravel.com/)

I want a fantastic sharp style that has great color blend and is attractive and matches my brand well.

The correct candidate will have access to my Canva Brand Kit and build templates inside of my account.

Also attached is a screenshot of my main color codes

The types of templates can include, but not be limited to the following:
BOTH DIGITAL FOR SOCIAL MEDIA AND PRINT VERSIONS
Listings flyers
Clients testimonials
market stats
open houses
Realtor Insights
Realtor analysis
sold properties
new listing properties
under contract properties
coming soon properties
Bullet points summarizing key data
Photo of the client at closing
Photo of the client at their home

Property Listing Template:

Description of the property
High-quality images
Key features and amenities
Open House Invitation:

Date, time, and location details
Compelling visuals of the property
Call-to-action for attendance
Just Sold Announcement:

Property details (address, price, etc.)
Celebratory message
Testimonials from satisfied clients
Testimonial Template:

Client testimonial
Photo of the client (with permission)
Brief background or story
Market Update Infographic:

Visual representation of current market trends
Realtor's insights and analysis
Buyer's Guide:

Step-by-step guide for homebuyers
Infographics explaining the buying process
Tips and advice for a successful purchase
Seller's Guide:

Information on preparing a home for sale
Infographics on the selling process
Tips for maximizing property value
Seasonal Greetings Template:

Personalized message for clients
Festive visuals or themes
Wishes for a successful year ahead
Neighborhood Highlight:

Showcase a specific neighborhood
Key attractions, schools, amenities
Testimonials from residents (if available)
Behind-the-Scenes:

Photos or videos of the realtor at work
Personalized messages about the real estate process
Humanizing content to connect with the audience
Infographic: Benefits of Working with a Realtor:

Visual representation of the advantages
Statistics or data supporting the benefits
Clear, concise points for easy consumption
Interactive Polls or Quizzes:

Engage the audience with fun polls
Real estate-related quizzes
Encourage interaction and sharing
Client Appreciation Post:

Thanking clients for their trust
Sharing success stories
Expressing gratitude with visuals
Video Tour Teaser:

Sneak peek of a property tour
Create excitement and anticipation

Target Market(s)

General Population ages 30-70

Requirements
Must have
• 60 plus designs
Nice to have
• 100 plus designs

```html
<!DOCTYPE html>
<html lang="en">
<head>
<meta charset="utf-8">
<title>Brindle Home Group – Listing &amp; Testimonial Templates</title>
<link rel="stylesheet" href="https://fonts.googleapis.com/css2?family=Lato:wght@400;700&family=Poppins:wght@400;500;600&display=swap">
<style>
:root{
  --stage:#adadad;
  --paper:#f6f6f6;
  --orange:#f29330;
  --ink:#141414;
  --grey:#6b6b6b;
  --white:#ffffff;
  --night-1:#2a3140;
  --night-2:#3b3f2c;
  --night-3:#4a3a22;
}
*{box-sizing:border-box;margin:0;padding:0}
html,body{width:839px;height:1200px;overflow:hidden;background:var(--stage)}
.canvas{position:relative;width:839px;height:1200px}
.panel{position:absolute;left:41px;width:753px;height:538px;overflow:hidden}

/* listing flyer */
.listing{top:41px;background:var(--paper);font-family:"Lato",sans-serif}
.listing .art{position:absolute;inset:0}
.brand{position:absolute;display:flex;align-items:center;gap:8px}
.listing .brand{left:69px;top:24px}
.brand-dot{width:62px;height:62px;border-radius:50%;background:var(--orange)}
.brand-name{font-weight:700;font-size:17px;line-height:1.15;letter-spacing:1px;color:var(--orange);text-transform:uppercase}
.address{position:absolute;left:69px;top:148px;font-weight:700;font-size:32px;color:var(--ink);letter-spacing:-0.5px}
.city{position:absolute;left:70px;top:199px;font-weight:700;font-size:16.5px;color:var(--grey)}
.status{position:absolute;left:68px;top:235px;font-weight:700;font-size:14px;color:var(--orange)}
.feature{position:absolute;width:100px;text-align:center;transform:translateX(-50%)}
.feature .icon{width:40px;height:40px;border-radius:50%;background:var(--ink);margin:0 auto;display:flex;align-items:center;justify-content:center}
.feature .icon svg{width:20px;height:20px}
.feature .label{margin-top:15px;font-size:10px;font-weight:700;color:var(--ink);white-space:nowrap}

/* testimonial */
.testimonial{top:617px;font-family:"Poppins",sans-serif;background:linear-gradient(160deg,var(--night-1) 0%,var(--night-2) 45%,var(--night-3) 100%)}
.testimonial .photo{position:absolute;inset:0;background:rgba(20,22,28,.45)}
.testimonial .brand{left:50%;top:12px;transform:translateX(-50%)}
.testimonial .brand-dot{width:63px;height:63px;background:var(--white)}
.testimonial .brand-name{font-family:"Poppins",sans-serif;font-weight:600;font-size:19px;color:var(--white);letter-spacing:1.5px}
.side-card{position:absolute;top:133px;height:143px;background:rgba(255,255,255,.14);border-radius:3px;padding:16px 14px;color:rgba(255,255,255,.28);font-size:8px;line-height:15.5px;text-align:center}
.side-card.left{left:42px;width:162px}
.side-card.right{left:532px;width:179px}
.side-card .who{margin-top:12px;font-weight:600;font-size:8.5px}
.quote-card{position:absolute;left:203px;top:117px;width:332px;height:172px;background:var(--white);border:2px solid var(--orange);border-radius:4px;padding:20px 18px 0}
.quote-mark{position:absolute;font-family:"Poppins",sans-serif;font-weight:600;font-size:44px;line-height:1;color:#bdbdbd}
.quote-mark.open{left:6px;top:0}
.quote-mark.close{left:218px;top:86px}
.quote-text{position:relative;font-family:"Lato",sans-serif;font-size:9.3px;line-height:18.3px;color:#222;text-align:center}
.author{position:absolute;left:46px;top:124px;display:flex;align-items:center;gap:10px}
.avatar{width:30px;height:30px;border-radius:50%;border:2px solid var(--orange);background:linear-gradient(135deg,#c9b8a6,#6f7d8c)}
.author-name{font-size:10px;color:var(--ink);font-weight:600}
.author-name span{font-weight:400;font-size:8.5px}
.author-place{font-size:7px;color:#9a9a9a}
.author-place .stars{color:var(--orange);letter-spacing:.5px;font-size:7.5px}
.peaks{position:absolute;left:0;bottom:0;width:753px;height:538px}
</style>
</head>
<body>
<div class="canvas">

  <section class="panel listing">
    <svg class="art" viewBox="0 0 753 538" aria-hidden="false">
      <circle cx="599" cy="207" r="253" fill="var(--orange)"/>
      <defs>
        <linearGradient id="homeTones" x1="0" y1="0" x2="0" y2="1">
          <stop offset="0" stop-color="#d9a45a"/>
          <stop offset=".35" stop-color="#b3653a"/>
          <stop offset=".6" stop-color="#5b5e55"/>
          <stop offset="1" stop-color="#4d6332"/>
        </linearGradient>
      </defs>
      <circle cx="628" cy="215" r="234" fill="url(#homeTones)" role="img" aria-label="Photo of the two-storey house at dusk with autumn trees and lawn"/>
      <circle cx="0" cy="538" r="96" fill="var(--orange)"/>
    </svg>

    <div class="brand"><div class="brand-dot"></div><div class="brand-name">Brindle<br>Home Group</div></div>

    <h1 class="address">30 E LARKIN CT</h1>
    <p class="city">KORAVEL SPRINGS, CO</p>
    <p class="status">Status: Active</p>

    <div class="feature" style="left:102px;top:270px">
      <div class="icon"><svg viewBox="0 0 20 20"><rect x="2" y="2" width="16" height="16" rx="3" fill="var(--orange)"/><path d="M6 14 14 6M9 6h5v5M6 9v5h5" stroke="var(--ink)" stroke-width="1.8" fill="none"/></svg></div>
      <div class="label">1,856 SQ. FEET</div>
    </div>
    <div class="feature" style="left:201px;top:270px">
      <div class="icon"><svg viewBox="0 0 20 20" fill="var(--orange)"><rect x="4" y="5" width="12" height="5" rx="1.5"/><rect x="2" y="10" width="16" height="4" rx="1"/><rect x="2" y="14" width="2" height="2"/><rect x="16" y="14" width="2" height="2"/></svg></div>
      <div class="label">3 BEDS</div>
    </div>
    <div class="feature" style="left:297px;top:270px">
      <div class="icon"><svg viewBox="0 0 20 20" fill="var(--orange)"><path d="M4 9V4a2 2 0 0 1 4 0" stroke="var(--orange)" stroke-width="1.5" fill="none"/><rect x="2" y="9" width="16" height="2" rx="1"/><path d="M3 12h14l-1.5 4h-11z"/></svg></div>
      <div class="label">2 BATHS</div>
    </div>
    <div class="feature" style="left:102px;top:358px">
      <div class="icon"><svg viewBox="0 0 20 20" fill="var(--orange)"><path d="M2 8 10 3l8 5v10h-3v-7H5v7H2z"/><rect x="6" y="12" width="8" height="4" rx="1"/></svg></div>
      <div class="label">3 GARAGE</div>
    </div>
    <div class="feature" style="left:201px;top:358px">
      <div class="icon"><svg viewBox="0 0 20 20"><path d="M10 2a5 5 0 0 1 5 5c0 4-5 8-5 8s-5-4-5-8a5 5 0 0 1 5-5z" fill="var(--orange)"/><circle cx="10" cy="7" r="2" fill="var(--ink)"/><ellipse cx="10" cy="17" rx="6" ry="1.5" fill="none" stroke="var(--orange)" stroke-width="1.3"/></svg></div>
      <div class="label">0.56 ACRES</div>
    </div>
    <div class="feature" style="left:297px;top:358px">
      <div class="icon"><svg viewBox="0 0 20 20" fill="var(--orange)"><path d="M10 3 1 11h3v6h4v-4h4v4h4v-6h3z"/></svg></div>
      <div class="label">1986 BUILT</div>
    </div>
  </section>

  <section class="panel testimonial">
    <div class="photo" role="img" aria-label="Dimmed photo of the house among aspen trees at dusk"></div>

    <div class="brand"><div class="brand-dot"></div><div class="brand-name">Brindle<br>Home Group</div></div>

    <div class="side-card left">
      Our team unsuccessfully tried to harvest our duckweed for several years trying different methods, then we purchased our Reedly in 2015. Reedly collected over 50 tons, it's worth the investment!
      <div class="who">- Owen Hale (Lake Management President)</div>
    </div>
    <div class="side-card right">
      Our team unsuccessfully tried to harvest our duckweed trying different methods, then we bought Reedly in 2015, within 3 months, the Reedly collected over 50 Tons of duckweed! Trust me, worth the investment!
      <div class="who">- Leo Castillo (Lake Management President)</div>
    </div>

    <div class="quote-card">
      <span class="quote-mark open">“</span>
      <span class="quote-mark close">”</span>
      <p class="quote-text">Temporibus autem quibusdam et aut officiis debitis aut rerum necessitatibus saepe eveniet ut et voluptates repudiandae sint et molestiae non recusandae. Itaque earum rerum hic tenetur a sapiente delectus, ut aut reiciendis voluptatibus maiores alias consequatur aut perferendis doloribus asperiores repellat.</p>
      <div class="author">
        <div class="avatar" role="img" aria-label="Client portrait"></div>
        <div>
          <div class="author-name">- Dale Renner <span>( Management President)</span></div>
          <div class="author-place">Village of Marrow Lake, Ohio <span class="stars">★★★★★</span></div>
        </div>
      </div>
    </div>

    <svg class="peaks" viewBox="0 0 753 538" aria-hidden="true">
      <polygon points="0,499 209,313 463,525 556,431 706,538 0,538" fill="var(--white)"/>
    </svg>
  </section>

</div>
</body>
</html>
```